BrightvaleHR Brochure

We need a Brochure design for a Human Resources company based in Windhoek Namibia. We do general HR admin, payroll, disciplinary hearings, recruitment. We would like a design which can be used to print hardcopies as well as pdf versions.

Industry/Entity Type

Human Resource

Colors

Designer to choose colors to be used in the design.

Requirements
Nice to have
• relevant pictures

```html
<!DOCTYPE html>
<html lang="en">
<head>
<meta charset="utf-8">
<title>BrightvaleHR Brochure Cover</title>
<link href="https://fonts.googleapis.com/css2?family=Cinzel:wght@500;600&family=Montserrat:wght@400&display=swap" rel="stylesheet">
<style>
  :root {
    --backdrop: #e6e7ea;
    --page-back: #f4f4f6;
    --page-front: #ffffff;
    --brand-blue: #3d68b0;
    --brand-blue-light: #7398d2;
    --ink-dark: #3a3a3c;
    --ink-text: #4a4a4e;
  }
  html, body {
    margin: 0;
    padding: 0;
    width: 996px;
    height: 1200px;
    overflow: hidden;
    background: var(--backdrop);
  }
  .canvas {
    position: relative;
    width: 996px;
    height: 1200px;
  }
  .spread {
    position: absolute;
    left: 0;
    top: 247px;
    width: 996px;
    height: 705px;
    box-shadow: 0 6px 24px rgba(0,0,0,0.18);
    overflow: hidden;
  }
  .spread-art {
    position: absolute;
    inset: 0;
  }
  .brand-name {
    position: absolute;
    font-family: "Cinzel", serif;
    font-weight: 600;
    color: var(--brand-blue);
    letter-spacing: 0.5px;
    white-space: nowrap;
    transform: translateX(-50%);
    margin: 0;
  }
  .brand-name--back { left: 247px; top: 365px; font-size: 24px; }
  .brand-name--front { left: 842px; top: 100px; font-size: 28px; }
  .headline {
    position: absolute;
    left: 747px;
    top: 540px;
    transform: translateX(-50%);
    margin: 0;
    text-align: center;
    font-family: "Cinzel", serif;
    font-weight: 600;
    line-height: 1;
  }
  .headline-top {
    display: block;
    color: var(--brand-blue);
    font-size: 36px;
    white-space: nowrap;
  }
  .headline-band {
    display: inline-block;
    margin-top: 2px;
    padding: 2px 8px 1px;
    background: var(--ink-dark);
    color: #ffffff;
    font-size: 32px;
    white-space: nowrap;
  }
  .intro {
    position: absolute;
    left: 747px;
    top: 624px;
    width: 470px;
    transform: translateX(-50%);
    margin: 0;
    text-align: center;
    font-family: "Montserrat", sans-serif;
    font-size: 12.5px;
    line-height: 15px;
    color: var(--ink-text);
    white-space: nowrap;
  }
  .contact-list {
    position: absolute;
    left: 40px;
    top: 660px;
    width: 440px;
    margin: 0;
    padding: 0;
    list-style: none;
    display: flex;
    gap: 16px;
    font-family: "Montserrat", sans-serif;
    font-size: 11.5px;
    color: var(--ink-text);
    white-space: nowrap;
  }
  .contact-item {
    display: flex;
    align-items: center;
    gap: 5px;
  }
  .contact-icon { width: 8px; height: 8px; fill: var(--brand-blue); }
</style>
</head>
<body>
<main class="canvas">
  <section class="spread">
    <svg class="spread-art" width="996" height="705" viewBox="0 0 996 705" xmlns="http://www.w3.org/2000/svg">
      <defs>
        <linearGradient id="backPage" x1="0" y1="0" x2="1" y2="1">
          <stop offset="0" stop-color="#fafafb"/>
          <stop offset="1" stop-color="#efeff2"/>
        </linearGradient>
        <linearGradient id="arcBlue" x1="0" y1="0" x2="1" y2="1">
          <stop offset="0" stop-color="#3a64ad"/>
          <stop offset="0.7" stop-color="#456fb6"/>
          <stop offset="1" stop-color="#7d9fd6"/>
        </linearGradient>
        <radialGradient id="photoTone" cx="0.5" cy="0.45" r="0.6">
          <stop offset="0" stop-color="#d7d8dc"/>
          <stop offset="0.6" stop-color="#c4c6cb"/>
          <stop offset="1" stop-color="#eeeeee"/>
        </radialGradient>
        <clipPath id="frontPage">
          <rect x="498" y="0" width="498" height="705"/>
        </clipPath>
      </defs>
      <rect class="back-cover" x="0" y="0" width="498" height="705" fill="url(#backPage)"/>
      <rect class="front-cover" x="498" y="0" width="498" height="705" fill="#ffffff"/>
      <g clip-path="url(#frontPage)">
        <circle class="cover-arc" cx="722" cy="190" r="320" fill="url(#arcBlue)"/>
        <g role="img" aria-label="Photo of a diverse office team celebrating with high fives around desks with computers">
          <circle cx="760" cy="203" r="260" fill="url(#photoTone)"/>
        </g>
      </g>
    </svg>

    <p class="brand-name brand-name--back">BrightvaleHR</p>
    <p class="brand-name brand-name--front">BrightvaleHR</p>

    <h1 class="headline">
      <span class="headline-top">Lorem Ipsum Dolor</span>
      <span class="headline-band">SIT AMET ADIPISCING</span>
    </h1>
    <p class="intro">sed do eiusmod tempor incididunt ut labore et dolore magna aliqua.<br>Ut enim ad minim veniam, quis nostrud exercitation ullamco laboris<br>nisi ut aliquip ex</p>

    <ul class="contact-list">
      <li class="contact-item">
        <svg class="contact-icon" viewBox="0 0 10 10"><circle cx="5" cy="5" r="4"/></svg>
        www.brightvalehr.com
      </li>
      <li class="contact-item">
        <svg class="contact-icon" viewBox="0 0 10 10"><rect x="0.5" y="2" width="9" height="6" rx="1"/></svg>
        info@brightvalehr.com
      </li>
      <li class="contact-item">
        <svg class="contact-icon" viewBox="0 0 10 10"><path d="M2 1h2l1 2.5-1.3 1a6 6 0 0 0 2.8 2.8l1-1.3L10 7v2a1 1 0 0 1-1 1A9 9 0 0 1 0 2a1 1 0 0 1 1-1z"/></svg>
        123-456-789
      </li>
    </ul>
  </section>
</main>
</body>
</html>
```